**** Business card design for LumaSoft ****

For my ICT company LumaSoft I need I need a business card design.

We design, build and host web-applications and we have our own CMS product.

Some good examples are attached.

The information should be:
Joren Velthuis
Managing director
E: j.velthuis@lumasoft-example.nl
M: +31(0)6 57182604
T: +31(0)40 7214589
W: www.lumasoft-example.nl

Address:
Pieter Dommelenlaan 27
5612 KT Eindhoven

Requirements
Must have
• - Use logo (see attachments)
- Double sided
- Distinctive
Nice to have
• - Place for a statement on the back-side: "Designed with knowledge, built with passion"
- HTML code (or Pagecraft)
- Dark (black or dark-gray) side
- Small simple images for telephone, e-mail en Url.
- QR code (only if not disturbing), not required, just an option

```html
<!DOCTYPE html>
<html lang="en">
<head>
<meta charset="utf-8">
<title>LumaSoft business card</title>
<link href="https://fonts.googleapis.com/css2?family=Cabin:wght@400&display=swap" rel="stylesheet">
<style>
  :root {
    --backdrop: #99a2a6;
    --card-dark: #0a0b0c;
    --card-light: #ffffff;
    --accent-blue: #3fa9e0;
    --text-dark: #1c1c1c;
    --brand-grey: #5f8b92;
  }
  html, body {
    margin: 0;
    padding: 0;
    width: 1200px;
    height: 900px;
    overflow: hidden;
    background: var(--backdrop);
    font-family: "Cabin", "Segoe UI", sans-serif;
  }
  .stage {
    position: relative;
    width: 1200px;
    height: 900px;
  }
  .card {
    position: absolute;
    top: 148px;
    width: 338px;
    height: 572px;
    border-radius: 40px;
  }
  .card--back {
    left: 240px;
    background: var(--card-dark);
  }
  .card--front {
    left: 646px;
    background: var(--card-light);
  }
  .back-brand {
    position: absolute;
    top: 228px;
    left: 0;
    width: 100%;
    text-align: center;
    font-size: 30px;
    color: var(--accent-blue);
  }
  .back-web {
    position: absolute;
    top: 333px;
    left: 0;
    width: 100%;
    text-align: center;
    font-size: 18px;
    color: var(--accent-blue);
  }
  .front-brand {
    position: absolute;
    top: 196px;
    left: 42px;
    display: flex;
    align-items: center;
    gap: 12px;
  }
  .front-brand__dot {
    width: 40px;
    height: 40px;
    border-radius: 50%;
    background: var(--accent-blue);
  }
  .front-brand__name {
    font-size: 28px;
    color: var(--brand-grey);
  }
  .details {
    position: absolute;
    left: 41px;
    top: 316px;
    font-size: 18px;
    line-height: 24px;
    color: var(--text-dark);
  }
  .details p { margin: 0; }
  .person__name { color: var(--accent-blue); }
  .address { margin-top: 34px !important; }
  .contact { margin-top: 10px; }
  .contact__label, .contact__at { color: var(--accent-blue); }
  .contact__email { font-size: 17px; }
</style>
</head>
<body>
<main class="stage">
  <section class="card card--back">
    <div class="back-brand">LumaSoft</div>
    <div class="back-web">www.lumasoft-example.nl</div>
  </section>

  <section class="card card--front">
    <div class="front-brand">
      <span class="front-brand__dot"></span>
      <span class="front-brand__name">LumaSoft</span>
    </div>
    <div class="details">
      <p class="person__name">Joren Velthuis</p>
      <p class="person__role">managing director</p>
      <p class="address">Pieter Dommelenlaan 27</p>
      <p>5612 KT Eindhoven</p>
      <div class="contact">
        <p><span class="contact__label">mob.</span> +31(0)40 7214589</p>
        <p><span class="contact__label">tel.</span> +31(0)6 57182604</p>
        <p class="contact__email">j.velthuis<span class="contact__at">@</span>lumasoft-example.nl</p>
      </div>
    </div>
  </section>
</main>
</body>
</html>
```